Painting Valtoni Renovations New buildings

Paint jobs plasterwork renovations new building customer painter paper drywall Entsorgungen.neukunden win color splash pleasure in colors competent clean fast reliable new try build demolition color combinations color concepts offers washing façade painting wood stains new projects old building renovations yes no beautiful new old sell secure solve paint over paint paint spray paint lye assemble disassemble sell buy trade oil dust new old assembly disassembly putty sanding fashion devastation copying belief feng shui kleopatra pompes beer colors swamp lime abrasion release tighten

Target Market(s)

construction industry

Contact Information for Business Card

Maler

Font styles to use
Serif

Colors
f04a50
959595

Requirements
Must have
• elegant appearance
Nice to have
• simply goal-oriented clientele in detail
Should not have
• too colorful

```html
<!DOCTYPE html>
<html lang="de">
<head>
<meta charset="utf-8">
<title>Valtoni Malerbetrieb – Visitenkarte</title>
<link href="https://fonts.googleapis.com/css2?family=Playfair+Display:wght@700&family=Dancing+Script:wght@600&family=Open+Sans:wght@400;600&display=swap" rel="stylesheet">
<style>
  :root {
    --stage: #2b2e33;
    --card-white: #ffffff;
    --card-black: #050505;
    --brand-blue: #2f56a3;
    --brand-blue-soft: #6f8fcc;
    --accent-pink: #d6338f;
    --accent-red: #f04a50;
    --accent-yellow: #f6d21e;
    --text-dark: #1d1d1f;
    --muted-grey: #959595;
  }
  html, body {
    margin: 0;
    width: 1200px;
    height: 900px;
    overflow: hidden;
    background: var(--stage);
  }
  .stage {
    position: relative;
    width: 1200px;
    height: 900px;
  }
  .card {
    position: absolute;
    top: 295px;
    width: 540px;
    height: 310px;
    border-radius: 4px;
    box-shadow: 0 14px 30px rgba(0,0,0,.45);
    overflow: hidden;
  }
  .card--front { left: 40px; background: var(--card-white); }
  .card--back  { left: 620px; background: var(--card-black); }

  .brand {
    position: absolute;
    display: flex;
    flex-direction: column;
    align-items: flex-start;
  }
  .brand__row { display: flex; align-items: center; gap: 10px; }
  .brand__name {
    font-family: "Playfair Display", Georgia, serif;
    font-weight: 700;
    color: var(--brand-blue);
    line-height: 1;
  }
  .brand__dot {
    border-radius: 50%;
    background: var(--accent-red);
  }
  .brand__tag {
    font-family: "Open Sans", Arial, sans-serif;
    font-weight: 600;
    color: var(--brand-blue);
    letter-spacing: .5px;
  }

  .card--front .brand { left: 34px; top: 40px; }
  .card--front .brand__name { font-size: 40px; }
  .card--front .brand__dot { width: 12px; height: 12px; }
  .card--front .brand__tag { font-size: 13px; margin: 4px 0 0 18px; }

  .card--back .brand { left: 50%; top: 50%; transform: translate(-50%, -50%); align-items: center; }
  .card--back .brand__name { font-size: 64px; }
  .card--back .brand__dot { width: 16px; height: 16px; }
  .card--back .brand__tag { font-size: 18px; color: var(--brand-blue-soft); margin-top: 6px; }

  .contact {
    position: absolute;
    left: 170px;
    top: 122px;
    font-family: "Open Sans", Arial, sans-serif;
  }
  .contact__name {
    font-family: "Dancing Script", cursive;
    font-weight: 600;
    font-size: 28px;
    color: var(--brand-blue);
    margin: 0;
    line-height: 1.1;
    white-space: nowrap;
  }
  .contact__title {
    font-size: 12px;
    font-weight: 600;
    color: var(--accent-pink);
    letter-spacing: .6px;
    margin: 2px 0 12px;
  }
  .contact__list { list-style: none; margin: 0; padding: 0; }
  .contact__item {
    display: flex;
    align-items: center;
    gap: 8px;
    font-size: 13px;
    color: var(--text-dark);
    margin-bottom: 7px;
    white-space: nowrap;
  }
  .contact__icon { width: 12px; height: 12px; flex: none; }

  .paint-artwork {
    position: absolute;
    left: 380px;
    top: 0;
    width: 160px;
    height: 310px;
    background: linear-gradient(180deg,
      rgba(240,74,80,.55) 0%,
      rgba(246,210,30,.45) 35%,
      rgba(111,143,204,.6) 65%,
      rgba(47,86,163,.75) 100%);
  }
</style>
</head>
<body>
<main class="stage">

  <section class="card card--front" aria-label="Visitenkarte Vorderseite">
    <div class="brand">
      <div class="brand__row">
        <span class="brand__name">Valtoni</span>
        <span class="brand__dot"></span>
      </div>
      <span class="brand__tag">Malerbetrieb</span>
    </div>

    <div class="contact">
      <p class="contact__name">Merenda Valtoni</p>
      <p class="contact__title">JOB TITLE</p>
      <ul class="contact__list">
        <li class="contact__item">
          <svg class="contact__icon" viewBox="0 0 12 12"><path d="M3 1 L5 3.5 L4 5 Q5 7 7 8 L8.5 7 L11 9 L9.5 11 Q4 10.5 1 3 Z" fill="var(--accent-red)"/></svg>
          000 000 0000
        </li>
        <li class="contact__item">
          <svg class="contact__icon" viewBox="0 0 12 12"><rect x="1" y="2.5" width="10" height="7" rx="1" fill="var(--accent-red)"/><path d="M1.5 3 L6 6.5 L10.5 3" stroke="#fff" stroke-width="1" fill="none"/></svg>
          youremail@xyz.com
        </li>
        <li class="contact__item">
          <svg class="contact__icon" viewBox="0 0 12 12"><circle cx="6" cy="6" r="5" fill="none" stroke="var(--accent-red)" stroke-width="1.2"/><ellipse cx="6" cy="6" rx="2" ry="5" fill="none" stroke="var(--accent-red)" stroke-width="1"/><line x1="1" y1="6" x2="11" y2="6" stroke="var(--accent-red)" stroke-width="1"/></svg>
          www.yourwebsite.com
        </li>
      </ul>
    </div>

    <div class="paint-artwork" role="img" aria-label="Illustration: Pinsel, der einen regenbogenfarbenen Farbbogen malt"></div>
  </section>

  <section class="card card--back" aria-label="Visitenkarte Rückseite">
    <div class="brand">
      <div class="brand__row">
        <span class="brand__name">Valtoni</span>
        <span class="brand__dot"></span>
      </div>
      <span class="brand__tag">Malerbetrieb</span>
    </div>
  </section>

</main>
</body>
</html>
```